Farm product labels

This is meant to design a set of labels for the following products:
Sachets (similar to Brannigan’s ketchup):
- Size: W4xH9 cm. This is the internal area (inside the four sealing borders) of sachets. Front side contains the design, and back side just texts with the ingredients, nutrition facts and origin. Please check check the attached pictures related to sachet designs for your reference!
- Products:
o Ketchup
o Honey
o Nubakora (chocolate spread made of cacao, peanuts, and milk)
o Peanut butter
o Fruit jam (either Mango, Guava or Passion fruit)

Stickers (to be added on transparent bags):
- Size: W8xH14 cm. It does not need to be rectangular
- It needs to accommodate small texts with the ingredients, nutrition facts and origin
- Products:
o Tomato paste
o Fruit pulp (either Mango, Guava or Passion fruit)
o Processed vegetables (either Yuca or Sweet potato). They are peeled, chopped, pre-boiled and frozen.

For those interested I’ll provide detailed info as required

Target Market(s)

Hotels. The sachets are specially for breakfast

Requirements
Must have
• All product label designs should:
- Show a similar look, reflecting a single source/branding
- Be attractive and be easy to recognize each product
- Contain the logo of our farm (uploaded)

```html
<!DOCTYPE html>
<html lang="en">
<head>
<meta charset="utf-8">
<title>Tomato Ketchup Sachets – Finca Valderrosa</title>
<link rel="stylesheet" href="https://fonts.googleapis.com/css2?family=Bebas+Neue&family=Gochi+Hand&display=swap">
<style>
  :root {
    --bg: #f6e4e4;
    --red: #e80000;
    --red-deep: #9a0000;
    --red-seal: #d10a0a;
    --silver-light: #f4f4f4;
    --silver-mid: #c9c9c9;
    --brand-blue: #0f2f8f;
    --white: #ffffff;
  }
  * { margin: 0; padding: 0; box-sizing: border-box; }
  html, body { width: 1200px; height: 876px; overflow: hidden; }
  body { background: var(--bg); position: relative; }

  .sachet {
    position: absolute;
    top: 127px;
    width: 284px;
    height: 604px;
  }
  .sachet--silver-top { left: 240px; }
  .sachet--all-red { left: 645px; }

  .sachet__shape { position: absolute; inset: 0; width: 284px; height: 604px; }

  .brand-mark {
    position: absolute;
    left: 0; right: 0;
    display: flex;
    flex-direction: column;
    align-items: center;
    gap: 6px;
  }
  .brand-mark__dot {
    width: 56px; height: 56px;
    border-radius: 50%;
  }
  .brand-mark__name {
    font-family: "Gochi Hand", cursive;
    font-size: 22px;
    line-height: 1;
    letter-spacing: 1px;
    text-transform: uppercase;
    text-align: center;
  }
  .brand-mark--blue .brand-mark__dot { background: var(--brand-blue); }
  .brand-mark--blue .brand-mark__name { color: var(--brand-blue); }
  .brand-mark--white .brand-mark__dot { background: var(--white); }
  .brand-mark--white .brand-mark__name { color: var(--white); }

  .product-name {
    position: absolute;
    left: 0; right: 0;
    text-align: center;
    color: var(--white);
  }
  .product-name__variety {
    display: block;
    font-family: "Gochi Hand", cursive;
    font-size: 46px;
    line-height: 1;
  }
  .product-name__type {
    display: block;
    font-family: "Bebas Neue", sans-serif;
    font-size: 70px;
    line-height: 0.9;
    margin-top: 2px;
  }

  .net-weight {
    position: absolute;
    left: 0; right: 0;
    top: 488px;
    text-align: center;
    color: var(--white);
    font-family: "Gochi Hand", cursive;
    font-size: 26px;
  }

  .sachet--silver-top .brand-mark--blue { top: 62px; }
  .sachet--silver-top .product-name { top: 270px; }
  .sachet--silver-top .brand-mark--white { top: 376px; }
  .sachet--all-red .brand-mark--white { top: 96px; }
  .sachet--all-red .product-name { top: 286px; }
</style>
</head>
<body>

<section class="sachet sachet--silver-top" aria-label="Tomato ketchup sachet with silver top">
  <svg class="sachet__shape" viewBox="0 0 284 604" aria-hidden="true">
    <defs>
      <linearGradient id="bodyRedA" x1="0" y1="0" x2="1" y2="1">
        <stop offset="0" stop-color="#ff0a0a"/>
        <stop offset="0.55" stop-color="#d40000"/>
        <stop offset="1" stop-color="#7e0000"/>
      </linearGradient>
      <linearGradient id="silverTop" x1="0" y1="0" x2="1" y2="0">
        <stop offset="0" stop-color="#bdbdbd"/>
        <stop offset="0.4" stop-color="#f6f6f6"/>
        <stop offset="1" stop-color="#c4c4c4"/>
      </linearGradient>
    </defs>
    <rect class="seal seal--top" x="0" y="0" width="284" height="31" fill="var(--silver-mid)"/>
    <path class="body" d="M2,31 L282,31 L270,60 L262,110 L262,520 L270,545 L282,572 L2,572 L14,545 L22,520 L22,110 L14,60 Z" fill="url(#bodyRedA)"/>
    <path class="silver-band" d="M2,31 L282,31 L270,60 L262,110 L262,148 Q140,212 22,156 L22,110 L14,60 Z" fill="url(#silverTop)"/>
    <rect class="seal seal--bottom" x="0" y="572" width="284" height="32" fill="var(--red-seal)"/>
  </svg>

  <div class="brand-mark brand-mark--blue">
    <span class="brand-mark__dot"></span>
    <span class="brand-mark__name">Finca Valderrosa</span>
  </div>

  <h2 class="product-name">
    <span class="product-name__variety">Tomato</span>
    <span class="product-name__type">Ketchup</span>
  </h2>

  <div class="brand-mark brand-mark--white">
    <span class="brand-mark__dot"></span>
    <span class="brand-mark__name">Finca Valderrosa</span>
  </div>

  <p class="net-weight">Net Wt. 20g</p>
</section>

<section class="sachet sachet--all-red" aria-label="Tomato ketchup sachet in full red">
  <svg class="sachet__shape" viewBox="0 0 284 604" aria-hidden="true">
    <defs>
      <linearGradient id="bodyRedB" x1="0" y1="0" x2="1" y2="1">
        <stop offset="0" stop-color="#ff0a0a"/>
        <stop offset="0.55" stop-color="#d40000"/>
        <stop offset="1" stop-color="#7e0000"/>
      </linearGradient>
    </defs>
    <rect class="seal seal--top" x="0" y="0" width="284" height="31" fill="var(--red-seal)"/>
    <path class="body" d="M2,31 L282,31 L270,60 L262,110 L262,520 L270,545 L282,572 L2,572 L14,545 L22,520 L22,110 L14,60 Z" fill="url(#bodyRedB)"/>
    <rect class="seal seal--bottom" x="0" y="572" width="284" height="32" fill="var(--red-seal)"/>
  </svg>

  <div class="brand-mark brand-mark--white">
    <span class="brand-mark__dot"></span>
    <span class="brand-mark__name">Finca Valderrosa</span>
  </div>

  <h2 class="product-name">
    <span class="product-name__variety">Tomato</span>
    <span class="product-name__type">Ketchup</span>
  </h2>

  <p class="net-weight">Net Wt. 20g</p>
</section>

</body>
</html>
```